Redesign trade show stand graphics for Harbour Panelworks

Update existing graphics of a trade show stand consisting of 2 walls. See the current design attached.

Left wall size is 2.4m high x 2700mm wide (made up of 3 pieces of 2400mm high x 900mm wide). The artwork will be printed on self adhesive stickers to cover the 2 walls.

NEW DESIGN LEFT WALL (2.4m high x 3m wide)
Headline at the top of the wall should read:
RENOVATE YOUR KITCHEN
the quick, easy and cost effective way:
JUST REPLACE THE DOORS and panels
• Cost effective: Save $$$
• Quick: approx. 15 working days
• Easy: No mess or inconvenience
• Polyurethane finish, unlimited choice of colours
• Measure, quote and install - DIY or contact our installers
• Delivery Australia wide
Harbour Panelworks logo at top of left and right walls. See logo attached. “Trueborn Goods” logo somewhere on the wall (logo attached)
The main body of the left wall will contain a “before” and “after” photo of a kitchen. Size of “before” shot approximately 250mm wide x 150mm high and “after” shot approximately 1m wide x 600mm high. Photo with higher resolution will be supplied.
Text:
• We replace doors, panels, drawer fronts and kickboards - all painted in polyurethane.
• We drill doors for new or existing hinges. We supply Kelto soft closing hinges, door handles, wardrobe door tracks and decorative items such as corbels, flutes and rosettes and capping.
• Our installers measure, quote and install or save money and do it yourself - DIY
Headline under the above: UPDATE YOUR BUILT IN WARDROBES WITH NEW DOORS
Sub headline: Custom made to your sizes and painted in polyurethane in the colour of your choice
2 photos of wardrobes to go under this headline

NEW DESIGN RIGHT WALL (2.4m high x 2800mm wide made up of 1 x 1000mm piece and 2 x 900mm pieces)
Visit our website: harbourpanelworks.com.au
Headline: SAVE TIME AND MONEY – REPLACE YOUR OLD DOORS (and panels)
Sub headline: WITH ONES PAINTED IN POLYURETHANE
Sub sub headline:
TO GET A QUOTE:
• DIY measure doors and panels and fill in our Quote Form or
• Contact our installers to measure, quote and install

At 1.5m high: 2 rows of 7 rectangular outlines 400mm high x 300mm wide (for sample doors that will be hung on the wall).
Directly under that, another headline:
Many more designs in our showroom at
47 Marlowe Avenue, Brindale Heights NSW 2871
Phone: (02) 9318 0627
Email: sales@harbourpanelworks.com.au
Website: harbourpanelworks.com.au
Place image of our showroom (attached) to the left or right.

“Trueborn Goods” logo and "Open Bench Club" logo somewhere on the wall (logos attached).
Small listing of approximately A5 size of “What we do”, “What we don’t do” and “What you do”. These will be supplied in bullet points.
Another image to use is uploaded below.

Target Market(s)

Home owners, home renovators

Industry/Entity Type

Trade

Font styles to use
Sans Serif
Other font styles liked:
• A font similar to that used on our website www.harbourpanelworks.com.au

Colors
f8972e

Requirements
Must have
• The background colour of the stand artwork should remain the same bright colour of our logo. The fonts should be similar to that used on our website www.harbourpanelworks.com.au
Nice to have
• Fun and engaging design

```html
<!DOCTYPE html>
<html lang="en">
<head>
<meta charset="utf-8">
<title>Harbour Panelworks – Trade Show Wall</title>
<link rel="stylesheet" href="https://fonts.googleapis.com/css2?family=Roboto+Condensed:wght@700&family=Open+Sans:wght@400;700&display=swap">
<style>
  :root {
    --backdrop: #a6a0a0;
    --brand-orange: #f78b3a;
    --soft-orange: #f9ad6d;
    --charcoal: #404042;
    --text-grey: #4a4a4c;
    --muted-grey: #58585a;
    --white: #ffffff;
    --quote-yellow: #fff200;
    --outline: rgba(220, 220, 220, 0.45);
  }
  * { margin: 0; padding: 0; box-sizing: border-box; }
  html, body { width: 1200px; height: 1000px; overflow: hidden; }
  body { background: var(--backdrop); position: relative; font-family: "Open Sans", Arial, sans-serif; }

  .wall { position: absolute; left: 92px; top: 92px; width: 1016px; height: 815px; background: var(--white); overflow: hidden; }
  .band { position: absolute; left: 0; width: 100%; }
  .band--header { top: 0; height: 173px; background: var(--brand-orange); }
  .band--samples { top: 173px; height: 213px; background: var(--charcoal); }
  .band--accent { top: 386px; height: 16px; background: var(--brand-orange); }
  .band--info { top: 402px; height: 236px; background: var(--soft-orange); }

  .headline-main { position: absolute; left: 98px; top: 20px; font-family: "Roboto Condensed", Arial, sans-serif; font-weight: 700; font-size: 54px; line-height: 50px; color: var(--charcoal); letter-spacing: -0.5px; }
  .headline-divider { position: absolute; left: 377px; top: 18px; width: 2px; height: 106px; background: var(--white); }
  .headline-side { position: absolute; left: 396px; top: 22px; font-family: "Roboto Condensed", Arial, sans-serif; font-weight: 700; font-size: 41px; line-height: 40px; color: var(--white); letter-spacing: -0.5px; }
  .headline-sub { position: absolute; left: 397px; top: 108px; font-weight: 700; font-size: 12.5px; color: var(--charcoal); letter-spacing: 0.1px; }

  .sample-grid { position: absolute; left: 96px; top: 141px; display: grid; grid-template-columns: repeat(7, 105px); grid-auto-rows: 140px; column-gap: 14px; row-gap: 12px; }
  .sample-slot { border: 1px solid var(--outline); }

  .website-line { position: absolute; left: 0; width: 100%; top: 446px; text-align: center; font-weight: 700; font-size: 26px; color: var(--text-grey); padding-right: 10px; }

  .showroom-frame { position: absolute; left: 60px; top: 508px; width: 456px; height: 278px; background: var(--white); padding: 9px; }
  .showroom-photo { width: 100%; height: 100%; background: linear-gradient(100deg, #3a3a3a 0%, #f2f0ea 12%, #e6e2d8 45%, #d9dbdc 70%, #60656a 100%); }

  .quote-badge { position: absolute; left: 541px; top: 502px; width: 144px; height: 144px; }
  .quote-text { position: absolute; left: 541px; top: 530px; width: 144px; text-align: center; transform: rotate(-10deg); font-family: "Roboto Condensed", Arial, sans-serif; font-weight: 700; font-size: 34px; line-height: 34px; color: var(--brand-orange); }

  .quote-steps { position: absolute; left: 700px; top: 518px; list-style: none; }
  .quote-steps li { position: relative; padding-left: 20px; font-weight: 700; font-size: 15px; line-height: 20px; color: var(--charcoal); margin-bottom: 21px; }
  .quote-steps li svg { position: absolute; left: 0; top: 2px; }

  .contact { position: absolute; left: 532px; top: 670px; color: var(--text-grey); }
  .contact-title { font-weight: 700; font-size: 20px; color: var(--muted-grey); }
  .contact-address { font-size: 14px; margin-top: 4px; }
  .contact-phone { font-weight: 700; font-size: 27px; color: var(--brand-orange); margin-top: 4px; line-height: 36px; }
  .contact-email { font-size: 14px; }

  .brand-mark { position: absolute; left: 888px; top: 660px; width: 100px; display: flex; flex-direction: column; align-items: center; gap: 8px; }
  .brand-mark-square { width: 34px; height: 34px; background: var(--brand-orange); }
  .brand-mark-name { font-family: "Roboto Condensed", Arial, sans-serif; font-weight: 700; font-size: 22px; line-height: 22px; color: var(--charcoal); text-align: center; }
</style>
</head>
<body>
  <main class="wall">
    <div class="band band--header"></div>
    <div class="band band--samples"></div>
    <div class="band band--accent"></div>
    <div class="band band--info"></div>

    <h1 class="headline-main">SAVE TIME<br>AND MONEY</h1>
    <div class="headline-divider"></div>
    <h2 class="headline-side">REPLACE YOUR OLD Kitchen<br>and Wardrobe DOORS and Panels</h2>
    <p class="headline-sub">WITH NEW CUSTOM MADE ONES PAINTED IN POLYURETHANE FINISH</p>

    <div class="sample-grid" aria-label="Sample door hanging positions">
      <div class="sample-slot"></div><div class="sample-slot"></div><div class="sample-slot"></div><div class="sample-slot"></div><div class="sample-slot"></div><div class="sample-slot"></div><div class="sample-slot"></div>
      <div class="sample-slot"></div><div class="sample-slot"></div><div class="sample-slot"></div><div class="sample-slot"></div><div class="sample-slot"></div><div class="sample-slot"></div><div class="sample-slot"></div>
    </div>

    <p class="website-line">Visit our website: harbourpanelworks.com.au</p>

    <div class="showroom-frame">
      <div class="showroom-photo" role="img" aria-label="Photo of the showroom with white wardrobe doors and a curved wall of sample panels"></div>
    </div>

    <svg class="quote-badge" viewBox="0 0 144 144" aria-hidden="true">
      <circle cx="72" cy="72" r="71" fill="#ffffff" stroke="#c8c8c8" stroke-width="1"/>
      <circle cx="72" cy="72" r="65" fill="var(--quote-yellow)"/>
    </svg>
    <p class="quote-text">TO GET<br>A QUOTE</p>

    <ul class="quote-steps">
      <li><svg width="12" height="18" viewBox="0 0 12 18"><path d="M0 0 L12 9 L0 18 Z" fill="#fff200"/></svg>DIY measure doors and panels<br>and fill in our Quote Form or</li>
      <li><svg width="12" height="18" viewBox="0 0 12 18"><path d="M0 0 L12 9 L0 18 Z" fill="#fff200"/></svg>Contact an installer to<br>measure, quote and install</li>
    </ul>

    <section class="contact">
      <p class="contact-title">More designs in our showroom</p>
      <p class="contact-address">47 Marlowe Avenue, Brindale Heights NSW 2871</p>
      <p class="contact-phone">Phone: (02) 9318 0627</p>
      <p class="contact-email">Email: sales@harbourpanelworks.com.au</p>
    </section>

    <div class="brand-mark">
      <div class="brand-mark-square"></div>
      <p class="brand-mark-name">Harbour<br>Panelworks</p>
    </div>
  </main>
</body>
</html>
```